Harbor Fellowship Business Cards
Heart Moved, Not Habit Held
Project: Harbor Fellowship Business Cards
Harbor Fellowship Business Cards -
Creative Brief
Professional
Harbor Fellowship
318 Millbrook Lane Providence, RI 02954
info@harborfelwcc.org
www.harborfelwcc.org
this will be a template to be used for all church departments. Please leave space for specific names of people, which will be added later.
Schedule of services Sunday: 10:00 a.m. - Sunday School 2:00 p.m. - Spanish service 6:00 p.m. - Service Tuesday 7:00 p.m. - Spanish Bible study Wednesday 7:00 p.m. - Bible study Thursday 7:30 p.m. - Prayer / Prayer station Saturday 7:00 p.m. - Spanish service

```html
<!DOCTYPE html>
<html lang="en">
<head>
<meta charset="utf-8">
<title>Harbor Fellowship Business Cards</title>
<link href="https://fonts.googleapis.com/css2?family=Open+Sans:wght@400;600;700&display=swap" rel="stylesheet">
<style>
  :root {
    --page: #f3f3f3;
    --charcoal: #333435;
    --charcoal-deep: #262728;
    --slate: #55575a;
    --gold: #e1c52c;
    --gold-text: #e4c830;
    --ink: #2b2b2b;
    --paper: #ffffff;
    --muted: #b8b8b8;
  }
  * { box-sizing: border-box; margin: 0; padding: 0; }
  html, body { width: 1200px; height: 618px; overflow: hidden; }
  body {
    background: var(--page);
    font-family: "Open Sans", Arial, sans-serif;
    position: relative;
  }
  .card {
    position: absolute;
    top: 166px;
    width: 500px;
    height: 286px;
    overflow: hidden;
    box-shadow: 0 6px 18px rgba(0,0,0,.12);
  }
  /* Front */
  .card--front {
    left: 60px;
    background: linear-gradient(160deg, var(--charcoal) 0%, var(--charcoal-deep) 100%);
    color: var(--paper);
  }
  .front__edge {
    position: absolute; right: 0; top: 0; width: 12px; height: 100%;
    background: var(--gold);
  }
  .front__brand { position: absolute; left: 36px; top: 78px; width: 240px; }
  .front__name {
    font-weight: 700; font-size: 38px; line-height: 1.1; letter-spacing: .3px;
  }
  .front__tagline {
    margin-top: 18px; font-size: 14px; color: var(--muted);
  }
  .front__divider {
    position: absolute; left: 292px; top: 62px; width: 2px; height: 162px;
    background: var(--slate);
  }
  .front__contact { position: absolute; left: 310px; top: 66px; width: 170px; font-size: 11px; line-height: 1.5; }
  .contact__person { font-size: 19px; font-weight: 600; color: var(--gold-text); line-height: 1.2; }
  .contact__role { font-size: 11px; color: var(--muted); margin-bottom: 12px; }
  .contact__address { color: #dcdcdc; margin-bottom: 12px; }
  .contact__label { color: var(--gold-text); display: inline-block; width: 38px; }
  .contact__line { color: #dcdcdc; white-space: nowrap; }
  /* Back */
  .card--back { left: 640px; background: var(--gold); color: var(--ink); }
  .back__header {
    position: absolute; left: 0; top: 28px; width: 100%; height: 46px;
    background: var(--slate);
    color: var(--paper); font-weight: 700; font-size: 17px;
    padding: 12px 24px;
  }
  .back__title { position: absolute; left: 24px; top: 92px; font-size: 18px; }
  .schedule { position: absolute; top: 126px; font-size: 12px; line-height: 1.5; }
  .schedule--left { left: 24px; }
  .schedule--right { left: 268px; top: 92px; }
  .schedule__day { font-weight: 700; }
  .schedule__group { margin-bottom: 8px; }
</style>
</head>
<body>
  <section class="card card--front" aria-label="Business card front">
    <div class="front__brand">
      <h1 class="front__name">Harbor<br>Fellowship</h1>
      <p class="front__tagline">Heart Moved, Not Habit Held</p>
    </div>
    <div class="front__divider"></div>
    <div class="front__contact">
      <p class="contact__person">Sam Porter</p>
      <p class="contact__role">Department</p>
      <p class="contact__address">318 Millbrook Lane<br>Providence, RI 02954</p>
      <p class="contact__line"><span class="contact__label">phone</span>(401) 555-0148</p>
      <p class="contact__line"><span class="contact__label">email</span>info@harborfelwcc.org</p>
      <p class="contact__line"><span class="contact__label">web</span>www.harborfelwcc.org</p>
    </div>
    <div class="front__edge"></div>
  </section>

  <section class="card card--back" aria-label="Business card back">
    <div class="back__header">Harbor Fellowship Community Church</div>
    <h2 class="back__title">Schedule of services</h2>
    <div class="schedule schedule--left">
      <div class="schedule__group">
        <p class="schedule__day">Sunday</p>
        <p>10:00 a.m. - Sunday School</p>
        <p>2:00 p.m. - Spanish service</p>
        <p>6:00 p.m. - Service</p>
      </div>
      <div class="schedule__group">
        <p class="schedule__day">Tuesday</p>
        <p>7:00 p.m. - Spanish Bible study</p>
      </div>
    </div>
    <div class="schedule schedule--right">
      <div class="schedule__group">
        <p class="schedule__day">Wednesday</p>
        <p>7:00 p.m. - Bible study</p>
      </div>
      <div class="schedule__group">
        <p class="schedule__day">Thursday</p>
        <p>7:30 p.m. - Prayer / Prayer station</p>
      </div>
      <div class="schedule__group">
        <p class="schedule__day">Saturday</p>
        <p>7:00 p.m. - Spanish service</p>
      </div>
    </div>
  </section>
</body>
</html>
```